We are opening a new restaurant concept called Lanternleaf - Fresh Asian Cuisine. Will be a trendy, casual dining restaurant (somewhat similar to a QR Morvins).
I have included pics of our logo in different formats and a picture of our front menu cover and inside menu as well as our actual menu in draft format. Need 6 individual pages total and letter size. Inside cover would be a "about us" type page that describes who we are and mission statement of restaurant (script unwritten at this time), Next page would be appetizers, inside page would have entrees on left and right side of book, then noodles/rice, vegetarian, kids and dessert section, last page would be drink/cocktail menu (still in progress).

```html
<!DOCTYPE html>
<html lang="en">
<head>
<meta charset="utf-8">
<title>Lanternleaf - Fresh Asian Cuisine · Menu Spreads</title>
<link rel="stylesheet" href="https://fonts.googleapis.com/css2?family=Fjalla+One&family=Open+Sans:wght@400;700&display=swap">
<style>
:root{
  --red:#d3141c;
  --red-dark:#a50e14;
  --black:#0d0d0d;
  --ink:#1c1c1c;
  --white:#ffffff;
  --grey:#a3a3a3;
  --row:rgba(255,255,255,.06);
  --stage:#e6e6e6;
}
*{box-sizing:border-box;margin:0;padding:0}
html,body{width:684px;height:1200px;overflow:hidden;background:var(--stage)}
.canvas{position:relative;width:684px;height:1200px;overflow:hidden;background:var(--stage)}

/* spread shell: designed at 660x426, scaled into place */
.spread{position:absolute;width:660px;height:426px;display:flex;transform-origin:0 0;
  background:radial-gradient(ellipse at 50% 45%,#2b2b2b 0%,#141414 55%,var(--black) 100%);
  box-shadow:0 6px 18px rgba(0,0,0,.28);overflow:hidden}
.spread.large{transform:scale(.82)}
.spread.small{transform:scale(.5)}
.page{position:relative;width:330px;height:426px}
.page + .page{border-left:1px solid #000}
.spread-band{position:absolute;left:0;top:0;width:660px;height:30px;background:var(--red);
  display:flex;align-items:center;justify-content:center;z-index:2}
.band{height:30px;background:var(--red);display:flex;align-items:center;justify-content:center}
.band-title{font-family:"Fjalla One",sans-serif;color:var(--white);font-size:20px;letter-spacing:.5px}
.page-body{padding:40px 12px 0 14px}

/* menu items */
.item{display:flex;align-items:center;justify-content:space-between;gap:8px;
  padding:3px 6px 3px 0;margin-bottom:4px;background:linear-gradient(90deg,var(--row),transparent 85%)}
.item-text{flex:1;min-width:0}
.name{font-family:"Fjalla One",sans-serif;color:var(--white);font-size:12.5px;line-height:1.2;
  border-left:2px solid var(--red);padding-left:5px}
.desc{font-family:"Open Sans",sans-serif;color:var(--grey);font-size:6.4px;line-height:1.3;padding-left:7px;margin-top:1px}
.price{flex:none;width:24px;height:24px;border-radius:50%;border:2px solid var(--red);
  display:flex;align-items:center;justify-content:center;
  font-family:"Open Sans",sans-serif;font-weight:700;font-size:9.5px;color:var(--white)}
.price.empty{width:26px;height:26px}
.appetizers .item{margin-bottom:7px}
.section-tag{display:inline-block;background:var(--red);color:var(--white);font-family:"Open Sans",sans-serif;
  font-weight:700;font-size:8px;letter-spacing:.6px;text-transform:uppercase;padding:2px 30px 2px 7px;margin:6px 0 5px}
.section-tag.first{margin-top:0}

/* drinks grid */
.drinks{display:grid;grid-template-columns:1fr 1fr;gap:6px 14px;padding:10px 12px 0 14px}
.drinks .item{margin:0}

/* kids / desserts / about page */
.kids-grid{display:grid;grid-template-columns:1fr 1fr;gap:0 12px;padding:7px 12px 0 14px;height:150px}
.kids-grid .item{margin-bottom:4px;min-height:27px}
.kids-grid .name{font-size:10.5px}
.kids-grid .desc{white-space:nowrap;overflow:hidden;text-overflow:ellipsis}
.kids-grid .price{width:21px;height:21px;font-size:8.5px}
.dessert-grid{display:grid;grid-template-columns:1fr 1fr;gap:4px 12px;padding:7px 12px 0 14px;height:80px}
.about-text{font-family:"Fjalla One",sans-serif;color:var(--white);font-size:10.5px;line-height:1.4;
  text-align:center;padding:8px 22px 0}
.contact-bar{position:absolute;left:0;bottom:0;width:330px;height:34px;background:var(--red);
  display:flex;align-items:center;justify-content:space-between;padding:0 12px;
  font-family:"Open Sans",sans-serif;color:var(--white);font-size:7px}
.contact-bar .line{display:flex;align-items:center;gap:4px}
.contact-bar .phone-num{font-family:"Fjalla One",sans-serif;font-size:11px}
.contact-bar svg{width:9px;height:9px;fill:var(--white)}
.contact-stack{display:flex;flex-direction:column;gap:3px}
.contact-right{text-align:right;display:flex;flex-direction:column;gap:3px}

/* cover */
.cover{display:flex;align-items:center;justify-content:center}
.brand-seal{width:190px;height:190px;border-radius:50%;background:var(--white);
  display:flex;flex-direction:column;align-items:center;justify-content:center;gap:6px}
.brand-name,.brand-tagline{font-family:"Fjalla One",sans-serif;color:var(--red);text-transform:uppercase}
.brand-name{font-size:30px;letter-spacing:1px}
.brand-tagline{font-size:12px;letter-spacing:2px}
</style>
</head>
<body>
<main class="canvas">

  <!-- Appetizers spread, large -->
  <section class="spread large appetizers" style="left:71px;top:20px">
    <div class="spread-band"><h2 class="band-title">Appetizers</h2></div>
    <div class="page"><div class="page-body">
      <div class="item"><div class="item-text"><p class="name">Edamame</p><p class="desc">Seasoned &amp; boiled soy bean</p></div><span class="price">$4</span></div>
      <div class="item"><div class="item-text"><p class="name">Scallion Pancakes</p><p class="desc">Traditional Chinese flatbread folded with oil and minced scallions and pan fried</p></div><span class="price">$6</span></div>
      <div class="item"><div class="item-text"><p class="name">Lanternleaf Lettuce Wraps</p><p class="desc">Seasoned ground chicken wrapped in lettuce and drizzled with our secret sauce</p></div><span class="price">$8</span></div>
      <div class="item"><div class="item-text"><p class="name">Salt &amp; Pepper Calamari</p><p class="desc">Crispy calamari with green &amp; red peppers and onions</p></div><span class="price">$9</span></div>
      <div class="item"><div class="item-text"><p class="name">Singapore Ribs</p><p class="desc">Tender baby back ribs in a sweet homemade glaze</p></div><span class="price">$9</span></div>
      <div class="item"><div class="item-text"><p class="name">Spicy Bang Bang Shrimp</p><p class="desc">Crispy fried shrimp tossed in our creamy spicy sauce</p></div><span class="price">$9</span></div>
      <div class="item"><div class="item-text"><p class="name">Drunken Chicken</p><p class="desc">Chicken, Thai chili and a house made spicy sauce</p></div><span class="price">$8</span></div>
      <div class="item"><div class="item-text"><p class="name">Sichuan Spiced Beef</p><p class="desc">Beef shank, beef tripe, cilantro, peanuts and celery</p></div><span class="price">$9</span></div>
      <div class="item"><div class="item-text"><p class="name">Beef Crispy Bottom Bow</p><p class="desc">Pan fried crispy bottom bao, stuffed with beef, drizzled with scallion and sesame</p></div><span class="price">$10</span></div>
    </div></div>
    <div class="page"><div class="page-body">
      <div class="item"><div class="item-text"><p class="name">Crispy Mala Beef Jerky</p><p class="desc">Dry fried shredded beef with fresh celery, Serrano peppers, garlic, green onion in soy sauce and peppercorn oil</p></div><span class="price">$9</span></div>
      <div class="item"><div class="item-text"><p class="name">Steamed Chicken Dumplings (6)</p><p class="desc">Chinese dumpling stuffed with chicken, Shiitake mushrooms and bamboo shoots</p></div><span class="price">$6</span></div>
      <div class="item"><div class="item-text"><p class="name">Red Oil Dumplings (6)</p><p class="desc">Pork filled dumplings in Sichuan red oil sauce drizzled with sesame</p></div><span class="price">$7</span></div>
      <div class="item"><div class="item-text"><p class="name">Pork Egg Rolls (2)</p><p class="desc">Hand rolled with julienned veggies served with our mustard sauce</p></div><span class="price">$4</span></div>
      <div class="item"><div class="item-text"><p class="name">Vegetarian Spring Rolls (3)</p><p class="desc">Fresh rice paper roll filled with vermicelli, bean sprouts and lettuce. Served with peanut sauce</p></div><span class="price">$4</span></div>
      <div class="item"><div class="item-text"><p class="name">Garlic Cucumber Salad</p><p class="desc">Sliced cucumber with a garlic vinaigrette</p></div><span class="price">$7</span></div>
      <div class="item"><div class="item-text"><p class="name">Lanternleaf Hot n' Sour Soup</p><p class="desc">Tangy broth with bamboo shoot, wood ear fungus, tofu, egg and carrots</p></div><span class="price">$4</span></div>
      <div class="item"><div class="item-text"><p class="name">West Lake Soup</p><p class="desc">Light creamy soup with ground beef, diced Shiitake mushrooms, tofu, bamboo shoots, egg white and cilantro</p></div><span class="price">$4</span></div>
    </div></div>
  </section>

  <!-- Back and front cover spread, large -->
  <section class="spread large" style="left:71px;top:385px">
    <div class="page">
      <div class="band"><h2 class="band-title">Kids Menu</h2></div>
      <div class="kids-grid">
        <div>
          <div class="item"><div class="item-text"><p class="name">Beef Lo Mein</p></div><span class="price">$5</span></div>
          <div class="item"><div class="item-text"><p class="name">Chicken Fried Rice</p></div><span class="price">$5</span></div>
          <div class="item"><div class="item-text"><p class="name">Sweet &amp; Sour Chicken</p></div><span class="price">$6</span></div>
          <div class="item"><div class="item-text"><p class="name">Lemon Chicken</p></div><span class="price">$6</span></div>
        </div>
        <div>
          <div class="item"><div class="item-text"><p class="name">Wall of Cake</p><p class="desc">Layered chocolate fudge cake</p></div><span class="price">$7</span></div>
          <div class="item"><div class="item-text"><p class="name">Wontons (4)</p><p class="desc">Fried wontons, sweet sauce</p></div><span class="price">$6</span></div>
          <div class="item"><div class="item-text"><p class="name">Tempura Snowball</p><p class="desc">Ice cream in crisp tempura</p></div><span class="price">$4</span></div>
          <div class="item"><div class="item-text"><p class="name">Patties in Caramel</p><p class="desc">Rice patties in warm caramel</p></div><span class="price">$7</span></div>
        </div>
      </div>
      <div class="band"><h2 class="band-title">Desserts</h2></div>
      <div class="dessert-grid">
        <div class="item"><div class="item-text"><p class="name">The Great</p><p class="desc">Scale this fortress of cake</p></div><span class="price empty"></span></div>
        <div class="item"><div class="item-text"><p class="name">Cheesecake</p><p class="desc">Fried wontons stuffed with vanilla ice cream</p></div><span class="price empty"></span></div>
        <div class="item"><div class="item-text"><p class="name">Sweet Rice</p><p class="desc">Traditional Chinese dessert</p></div><span class="price empty"></span></div>
      </div>
      <div class="band"><h2 class="band-title">About us</h2></div>
      <p class="about-text">Lorem Ipsum is simply dummy text of the printing and typesetting industry. Lorem Ipsum has been the industry's standard dummy text ever since the 1500s.</p>
      <div class="contact-bar">
        <div class="contact-stack">
          <span class="line"><svg viewBox="0 0 10 10"><path d="M5 0a3.5 3.5 0 0 0-3.5 3.5C1.5 6 5 10 5 10s3.5-4 3.5-6.5A3.5 3.5 0 0 0 5 0zm0 5a1.5 1.5 0 1 1 0-3 1.5 1.5 0 0 1 0 3z"/></svg>Shop# ABC 1234, City, Country</span>
          <span class="line"><svg viewBox="0 0 10 10"><path d="M2 0l2 2.5-1 1.2c.6 1.3 1.5 2.2 2.8 2.8l1.2-1L10 7.5 8.6 9.6C4.5 10 0 5.5.4 1.4z"/></svg><span class="phone-num">0 123 456 7890</span></span>
        </div>
        <div class="contact-right"><span>www.lanternleaf.com</span><span>@lanternleaf</span></div>
      </div>
    </div>
    <div class="page cover">
      <div class="brand-seal"><p class="brand-name">Lanternleaf</p><p class="brand-tagline">Fresh Asian Cuisine</p></div>
    </div>
  </section>

  <!-- Grid: cover / kids -->
  <section class="spread small" style="left:8px;top:752px">
    <div class="page cover">
      <div class="brand-seal"><p class="brand-name">Lanternleaf</p><p class="brand-tagline">Fresh Asian Cuisine</p></div>
    </div>
    <div class="page">
      <div class="band"><h2 class="band-title">Kids Menu</h2></div>
      <div class="kids-grid">
        <div>
          <div class="item"><div class="item-text"><p class="name">Beef Lo Mein</p></div><span class="price">$5</span></div>
          <div class="item"><div class="item-text"><p class="name">Chicken Fried Rice</p></div><span class="price">$5</span></div>
          <div class="item"><div class="item-text"><p class="name">Sweet &amp; Sour Chicken</p></div><span class="price">$6</span></div>
          <div class="item"><div class="item-text"><p class="name">Lemon Chicken</p></div><span class="price">$6</span></div>
        </div>
        <div>
          <div class="item"><div class="item-text"><p class="name">Wall of Cake</p><p class="desc">Layered chocolate fudge cake</p></div><span class="price">$7</span></div>
          <div class="item"><div class="item-text"><p class="name">Wontons (4)</p><p class="desc">Fried wontons, sweet sauce</p></div><span class="price">$6</span></div>
          <div class="item"><div class="item-text"><p class="name">Tempura Snowball</p><p class="desc">Ice cream in crisp tempura</p></div><span class="price">$4</span></div>
          <div class="item"><div class="item-text"><p class="name">Patties in Caramel</p><p class="desc">Rice patties in warm caramel</p></div><span class="price">$7</span></div>
        </div>
      </div>
      <div class="band"><h2 class="band-title">Desserts</h2></div>
      <div class="dessert-grid">
        <div class="item"><div class="item-text"><p class="name">The Great</p><p class="desc">Scale this fortress of cake</p></div><span class="price empty"></span></div>
        <div class="item"><div class="item-text"><p class="name">Cheesecake</p><p class="desc">Fried wontons stuffed with vanilla ice cream</p></div><span class="price empty"></span></div>
        <div class="item"><div class="item-text"><p class="name">Sweet Rice</p><p class="desc">Traditional Chinese dessert</p></div><span class="price empty"></span></div>
      </div>
      <div class="band"><h2 class="band-title">About us</h2></div>
      <p class="about-text">Lorem Ipsum is simply dummy text of the printing and typesetting industry. Lorem Ipsum has been the industry's standard dummy text ever since the 1500s.</p>
      <div class="contact-bar">
        <div class="contact-stack">
          <span class="line"><svg viewBox="0 0 10 10"><path d="M5 0a3.5 3.5 0 0 0-3.5 3.5C1.5 6 5 10 5 10s3.5-4 3.5-6.5A3.5 3.5 0 0 0 5 0zm0 5a1.5 1.5 0 1 1 0-3 1.5 1.5 0 0 1 0 3z"/></svg>Shop# ABC 1234, City, Country</span>
          <span class="line"><svg viewBox="0 0 10 10"><path d="M2 0l2 2.5-1 1.2c.6 1.3 1.5 2.2 2.8 2.8l1.2-1L10 7.5 8.6 9.6C4.5 10 0 5.5.4 1.4z"/></svg><span class="phone-num">0 123 456 7890</span></span>
        </div>
        <div class="contact-right"><span>www.lanternleaf.com</span><span>@lanternleaf</span></div>
      </div>
    </div>
  </section>

  <!-- Grid: entrees, chef specialties / chicken -->
  <section class="spread small" style="left:346px;top:752px">
    <div class="spread-band"><h2 class="band-title">Entrees</h2></div>
    <div class="page"><div class="page-body">
      <span class="section-tag first">Chef Specialties</span>
      <div class="item"><div class="item-text"><p class="name">Jasmine Tea Smoked Duck</p><p class="desc">Boneless half duck smoked with jasmine tea, served with scallion pancakes</p></div><span class="price">$24</span></div>
      <div class="item"><div class="item-text"><p class="name">Sizzling Cumin Lamb</p><p class="desc">Tender lamb stir fried with cumin, chili peppers and onions</p></div><span class="price">$16</span></div>
      <div class="item"><div class="item-text"><p class="name">Chef Su's Spicy Beef</p><p class="desc">Sliced beef simmered in a house made red peppercorn broth</p></div><span class="price">$16</span></div>
      <div class="item"><div class="item-text"><p class="name">Chef Su's Spicy Fish</p><p class="desc">Fish fillet poached in red peppercorn broth with Thai chili</p></div><span class="price">$17</span></div>
      <div class="item"><div class="item-text"><p class="name">General Tso's Scallops</p><p class="desc">Crispy scallops tossed in a sweet and tangy chili sauce</p></div><span class="price">$18</span></div>
      <div class="item"><div class="item-text"><p class="name">Shanghai Chili Lettuce Wraps</p><p class="desc">Chicken, shrimp and shiitake in a spicy glaze with lettuce leaves</p></div><span class="price">$16</span></div>
      <span class="section-tag">Beef &amp; Pork</span>
      <div class="item"><div class="item-text"><p class="name">Dancing Beef</p><p class="desc">Angus beef on a bed of sizzling rice crackers</p></div><span class="price">$16</span></div>
      <div class="item"><div class="item-text"><p class="name">Oyster Beef</p><p class="desc">Tender beef and mushrooms in a homemade oyster sauce</p></div><span class="price">$14</span></div>
      <div class="item"><div class="item-text"><p class="name">Dancing Pork Belly</p><p class="desc">Braised pork belly on sizzling rice crackers</p></div><span class="price">$15</span></div>
    </div></div>
    <div class="page"><div class="page-body">
      <div class="item"><div class="item-text"><p class="name">Double Pepper Beef</p><p class="desc">Beef with fresh green peppercorns and Thai chili</p></div><span class="price">$16</span></div>
      <div class="item"><div class="item-text"><p class="name">Sweet &amp; Sour Baby Back Ribs</p><p class="desc">Tender baby back ribs in a sweet and sour glaze</p></div><span class="price">$16</span></div>
      <div class="item"><div class="item-text"><p class="name">Twice Cooked Pork</p><p class="desc">Pork belly with leeks and fermented black beans</p></div><span class="price">$14</span></div>
      <span class="section-tag">Chicken</span>
      <div class="item"><div class="item-text"><p class="name">Kung Pao Chicken</p><p class="desc">Chicken with roasted peanuts, scallions and dry red chili</p></div><span class="price">$13</span></div>
      <div class="item"><div class="item-text"><p class="name">Orange Chicken</p><p class="desc">Battered chicken in a tangy orange flavored sauce</p></div><span class="price">$13</span></div>
      <div class="item"><div class="item-text"><p class="name">Double Pepper Chicken</p><p class="desc">Chicken with fresh green peppercorns and jalapenos</p></div><span class="price">$15</span></div>
      <div class="item"><div class="item-text"><p class="name">Crispy Spicy Chicken</p><p class="desc">Crispy chicken with Sichuan peppers and cilantro</p></div><span class="price">$14</span></div>
      <div class="item"><div class="item-text"><p class="name">General Tso's Chicken</p><p class="desc">Fried chicken in a sweet and tangy chili sauce</p></div><span class="price">$13</span></div>
      <div class="item"><div class="item-text"><p class="name">Shredded Chicken in Spicy Garlic Sauce</p><p class="desc">Shredded chicken, wood ear and bamboo shoots</p></div><span class="price">$14</span></div>
    </div></div>
  </section>

  <!-- Grid: entrees, seafood / vegetarian / drinks -->
  <section class="spread small" style="left:8px;top:971px">
    <div class="spread-band"><h2 class="band-title">Entrees</h2></div>
    <div class="page"><div class="page-body">
      <span class="section-tag first">Seafood</span>
      <div class="item"><div class="item-text"><p class="name">Kung Pao Shrimp</p><p class="desc">Shrimp with roasted peanuts, dry red chili and scallions</p></div><span class="price">$16</span></div>
      <div class="item"><div class="item-text"><p class="name">Rice Wine Shrimp &amp; Tofu</p><p class="desc">Shrimp and tofu braised in a light rice wine sauce</p></div><span class="price">$18</span></div>
      <div class="item"><div class="item-text"><p class="name">Shrimp in Spicy Garlic Sauce</p><p class="desc">Shrimp with pickled peppers, garlic and scallions</p></div><span class="price">$15</span></div>
      <div class="item"><div class="item-text"><p class="name">Lemon Peel Shrimp</p><p class="desc">Crispy shrimp tossed in our lemon peel sauce</p></div><span class="price">$16</span></div>
      <div class="item"><div class="item-text"><p class="name">Rice Wine Fish</p><p class="desc">White fish fillet braised in rice wine</p></div><span class="price">$14</span></div>
      <span class="section-tag">Noodles &amp; Rice</span>
      <div class="item"><div class="item-text"><p class="name">Lanternleaf's Fried Rice</p><p class="desc">Shrimp, chicken and beef with egg and onions</p></div><span class="price">$12</span></div>
      <div class="item"><div class="item-text"><p class="name">Vegetarian White Fried Rice</p><p class="desc">Mixed vegetables with jasmine rice</p></div><span class="price">$10</span></div>
      <div class="item"><div class="item-text"><p class="name">Lanternleaf's Lo Mein</p><p class="desc">Shrimp, chicken and beef with scallions</p></div><span class="price">$12</span></div>
      <div class="item"><div class="item-text"><p class="name">Vegetarian Lo Mein</p><p class="desc">Mixed vegetables with egg noodles</p></div><span class="price">$10</span></div>
    </div></div>
    <div class="page"><div class="page-body">
      <span class="section-tag first">Vegetarian Dishes</span>
      <div class="item"><div class="item-text"><p class="name">Wok Tossed String Beans</p><p class="desc">Fresh string beans with pickled vegetables</p></div><span class="price">$9</span></div>
      <div class="item"><div class="item-text"><p class="name">Mapo Tofu</p><p class="desc">Soft tofu, scallions and Sichuan peppers</p></div><span class="price">$11</span></div>
      <div class="item"><div class="item-text"><p class="name">Spicy Garlic Eggplant</p><p class="desc">Chinese eggplant in spicy garlic sauce</p></div><span class="price">$12</span></div>
      <div class="item"><div class="item-text"><p class="name">Buddha's Delight</p><p class="desc">Seasonal vegetables in a light soy sauce</p></div><span class="price">$10</span></div>
      <div class="item"><div class="item-text"><p class="name">Stir-fried Eggplant Beans</p><p class="desc">Eggplant and string beans with garlic</p></div><span class="price">$12</span></div>
      <div class="item"><div class="item-text"><p class="name">Shiitake Baby Bok-Choy</p><p class="desc">Baby bok choy with shiitake in brown sauce</p></div><span class="price">$12</span></div>
    </div>
      <div class="band" style="margin-top:8px"><h2 class="band-title">Drink/Cocktail menu</h2></div>
      <div class="drinks">
        <div class="item"><div class="item-text"><p class="name">Lorem Ipsum</p></div><span class="price">$6</span></div>
        <div class="item"><div class="item-text"><p class="name">Lorem Ipsum</p></div><span class="price">$6</span></div>
        <div class="item"><div class="item-text"><p class="name">Lorem Ipsum</p></div><span class="price">$6</span></div>
        <div class="item"><div class="item-text"><p class="name">Lorem Ipsum</p></div><span class="price">$6</span></div>
        <div class="item"><div class="item-text"><p class="name">Lorem Ipsum</p></div><span class="price">$6</span></div>
        <div class="item"><div class="item-text"><p class="name">Lorem Ipsum</p></div><span class="price">$6</span></div>
      </div>
    </div>
  </section>

  <!-- Grid: appetizers -->
  <section class="spread small appetizers" style="left:346px;top:971px">
    <div class="spread-band"><h2 class="band-title">Appetizers</h2></div>
    <div class="page"><div class="page-body">
      <div class="item"><div class="item-text"><p class="name">Edamame</p><p class="desc">Seasoned &amp; boiled soy bean</p></div><span class="price">$4</span></div>
      <div class="item"><div class="item-text"><p class="name">Scallion Pancakes</p><p class="desc">Traditional Chinese flatbread folded with oil and minced scallions and pan fried</p></div><span class="price">$6</span></div>
      <div class="item"><div class="item-text"><p class="name">Lanternleaf Lettuce Wraps</p><p class="desc">Seasoned ground chicken wrapped in lettuce and drizzled with our secret sauce</p></div><span class="price">$8</span></div>
      <div class="item"><div class="item-text"><p class="name">Salt &amp; Pepper Calamari</p><p class="desc">Crispy calamari with green &amp; red peppers and onions</p></div><span class="price">$9</span></div>
      <div class="item"><div class="item-text"><p class="name">Singapore Ribs</p><p class="desc">Tender baby back ribs in a sweet homemade glaze</p></div><span class="price">$9</span></div>
      <div class="item"><div class="item-text"><p class="name">Spicy Bang Bang Shrimp</p><p class="desc">Crispy fried shrimp tossed in our creamy spicy sauce</p></div><span class="price">$9</span></div>
      <div class="item"><div class="item-text"><p class="name">Drunken Chicken</p><p class="desc">Chicken, Thai chili and a house made spicy sauce</p></div><span class="price">$8</span></div>
      <div class="item"><div class="item-text"><p class="name">Sichuan Spiced Beef</p><p class="desc">Beef shank, beef tripe, cilantro, peanuts and celery</p></div><span class="price">$9</span></div>
      <div class="item"><div class="item-text"><p class="name">Beef Crispy Bottom Bow</p><p class="desc">Pan fried crispy bottom bao, stuffed with beef, drizzled with scallion and sesame</p></div><span class="price">$10</span></div>
    </div></div>
    <div class="page"><div class="page-body">
      <div class="item"><div class="item-text"><p class="name">Crispy Mala Beef Jerky</p><p class="desc">Dry fried shredded beef with fresh celery, Serrano peppers, garlic, green onion in soy sauce and peppercorn oil</p></div><span class="price">$9</span></div>
      <div class="item"><div class="item-text"><p class="name">Steamed Chicken Dumplings (6)</p><p class="desc">Chinese dumpling stuffed with chicken, Shiitake mushrooms and bamboo shoots</p></div><span class="price">$6</span></div>
      <div class="item"><div class="item-text"><p class="name">Red Oil Dumplings (6)</p><p class="desc">Pork filled dumplings in Sichuan red oil sauce drizzled with sesame</p></div><span class="price">$7</span></div>
      <div class="item"><div class="item-text"><p class="name">Pork Egg Rolls (2)</p><p class="desc">Hand rolled with julienned veggies served with our mustard sauce</p></div><span class="price">$4</span></div>
      <div class="item"><div class="item-text"><p class="name">Vegetarian Spring Rolls (3)</p><p class="desc">Fresh rice paper roll filled with vermicelli, bean sprouts and lettuce. Served with peanut sauce</p></div><span class="price">$4</span></div>
      <div class="item"><div class="item-text"><p class="name">Garlic Cucumber Salad</p><p class="desc">Sliced cucumber with a garlic vinaigrette</p></div><span class="price">$7</span></div>
      <div class="item"><div class="item-text"><p class="name">Lanternleaf Hot n' Sour Soup</p><p class="desc">Tangy broth with bamboo shoot, wood ear fungus, tofu, egg and carrots</p></div><span class="price">$4</span></div>
      <div class="item"><div class="item-text"><p class="name">West Lake Soup</p><p class="desc">Light creamy soup with ground beef, diced Shiitake mushrooms, tofu, bamboo shoots, egg white and cilantro</p></div><span class="price">$4</span></div>
    </div></div>
  </section>

</main>
</body>
</html>
```